Business Card Designs

Looking to design a 3.5" x 2" standard business card for our employees.
The design needs to be sleek, simple, and modern. We would like our logo (attached) to be incorporated, but not in that colour, rather an outline of the logo in either gold or silver (whichever looks better).

Modern and Simple is what we are looking for, but be creative in incorporating the logo.

```html
<!DOCTYPE html>
<html lang="en">
<head>
<meta charset="utf-8">
<title>Lakeview Suite Residences — Business Card</title>
<link href="https://fonts.googleapis.com/css2?family=Lato:wght@400;700;900&display=swap" rel="stylesheet">
<style>
  :root {
    --stage: #ececec;
    --card-dark: #2b2b2d;
    --card-dark-deep: #1f1f21;
    --gold-light: #f2d47a;
    --gold: #d4a52a;
    --gold-deep: #a9791a;
    --silver: #e4e4e4;
    --silver-deep: #9a9a9a;
    --ink-on-gold: #2a2317;
    --text-light: #f4f4f4;
  }
  * { margin: 0; padding: 0; box-sizing: border-box; }
  html, body { width: 1200px; height: 802px; overflow: hidden; }
  body {
    background: var(--stage);
    font-family: "Lato", sans-serif;
    position: relative;
  }
  .card {
    position: absolute;
    top: 246px;
    width: 540px;
    height: 309px;
    border-radius: 3px;
    overflow: hidden;
    box-shadow: 0 6px 18px rgba(0,0,0,0.18);
  }
  .card-front { left: 45px; background: var(--card-dark); }
  .card-back { left: 615px; }

  .front-wave { position: absolute; inset: 0; width: 540px; height: 309px; }

  .brand {
    position: absolute;
    left: 42px;
    top: 196px;
    display: flex;
    align-items: center;
    gap: 10px;
  }
  .brand-mark {
    width: 14px; height: 14px;
    background: var(--gold);
  }
  .brand-name {
    color: var(--gold);
    font-weight: 700;
    font-size: 17px;
    letter-spacing: 2px;
    line-height: 1.25;
    text-transform: uppercase;
  }

  .identity {
    position: absolute;
    right: 30px;
    top: 20px;
    text-align: right;
    color: var(--text-light);
  }
  .identity-name {
    color: var(--gold);
    font-weight: 900;
    font-size: 17px;
    letter-spacing: 0.5px;
    text-transform: uppercase;
  }
  .identity-role { font-size: 13px; margin-top: 2px; }
  .identity-address { font-size: 13px; line-height: 1.35; margin-top: 10px; }

  .contact {
    position: absolute;
    right: 30px;
    bottom: 24px;
    list-style: none;
    color: var(--ink-on-gold);
    font-size: 13px;
    text-align: right;
  }
  .contact li {
    display: flex;
    justify-content: flex-end;
    align-items: center;
    gap: 8px;
    line-height: 1.55;
  }
  .contact-icon {
    width: 12px; height: 12px;
    fill: var(--ink-on-gold);
  }

  .back-surface {
    position: absolute; inset: 0;
    background: radial-gradient(ellipse at 60% 40%, #333335 0%, var(--card-dark) 55%, var(--card-dark-deep) 100%);
  }
  .back-brand {
    position: absolute;
    right: 80px;
    top: 50%;
    transform: translateY(-50%);
    color: var(--gold);
    font-weight: 700;
    font-size: 15px;
    letter-spacing: 2px;
    text-transform: uppercase;
    text-align: right;
    line-height: 1.3;
  }
</style>
</head>
<body>

  <section class="card card-front" aria-label="Business card front">
    <svg class="front-wave" viewBox="0 0 540 309" aria-hidden="true">
      <defs>
        <linearGradient id="goldSheen" x1="0" y1="1" x2="1" y2="0">
          <stop offset="0" stop-color="var(--gold-deep)"/>
          <stop offset="0.45" stop-color="var(--gold)"/>
          <stop offset="0.75" stop-color="var(--gold-light)"/>
          <stop offset="1" stop-color="var(--gold)"/>
        </linearGradient>
        <linearGradient id="silverSheen" x1="0" y1="1" x2="1" y2="0">
          <stop offset="0" stop-color="var(--silver-deep)"/>
          <stop offset="0.5" stop-color="var(--silver)"/>
          <stop offset="1" stop-color="var(--silver-deep)"/>
        </linearGradient>
      </defs>
      <path d="M180,309 C250,300 296,230 336,190 C378,150 445,112 540,108 L540,118 C450,122 385,158 344,196 C304,236 262,302 200,309 Z" fill="url(#silverSheen)"/>
      <path d="M212,309 C272,300 310,240 350,200 C390,165 450,130 540,125 L540,309 Z" fill="url(#goldSheen)"/>
    </svg>

    <div class="brand">
      <span class="brand-mark" aria-hidden="true"></span>
      <span class="brand-name">Lakeview Suite<br>Residences</span>
    </div>

    <div class="identity">
      <p class="identity-name">Daniel Carter</p>
      <p class="identity-role">Manager</p>
      <p class="identity-address">Your Address, City<br>State, Zip 0000</p>
    </div>

    <ul class="contact">
      <li>555-010-4821
        <svg class="contact-icon" viewBox="0 0 12 12" aria-hidden="true"><path d="M2.5 1h2l1 2.5-1.2 1a6 6 0 0 0 3.2 3.2l1-1.2L11 7.5v2a1 1 0 0 1-1 1A9 9 0 0 1 1.5 2a1 1 0 0 1 1-1z"/></svg>
      </li>
      <li>contact@mailbox.net
        <svg class="contact-icon" viewBox="0 0 12 12" aria-hidden="true"><path d="M1 2.5h10v7H1z M1.6 3l4.4 3.3L10.4 3"/></svg>
      </li>
      <li>www.lakeviewsuites.ca
        <svg class="contact-icon" viewBox="0 0 12 12" aria-hidden="true"><circle cx="6" cy="6" r="5"/></svg>
      </li>
    </ul>
  </section>

  <section class="card card-back" aria-label="Business card back">
    <div class="back-surface" role="img" aria-label="Dark tonal embossed repeat pattern of the company monogram"></div>
    <p class="back-brand">Lakeview Suite<br>Residences</p>
  </section>

</body>
</html>
```